Tide & Stone Subtitle Walk the Road of Still Waters

This is a spiritual book. It opens with a question for the readers -- Are you happy? Then proceeds to discuss the meaning of happiness, why the majority isn't and ways to achieve it. The work offers hope, and actual answers. In that regard the cover needs to relate those things.

I'm happy to contribute by answering further questions and making suggestions, however, am open to the designer letting their Spirit soar and see where it leads them.

Ask yourself the question; Am I happy, imagine finding Your happiness then designing the cover that comes from that space. Just a thought.

```html
<!DOCTYPE html>
<html lang="en">
<head>
<meta charset="utf-8">
<title>Tide &amp; Stone — Cover Spread</title>
<link rel="stylesheet" href="https://fonts.googleapis.com/css2?family=Cormorant+Garamond:wght@600&family=Open+Sans:wght@400;700&display=swap">
<style>
  :root {
    --backdrop: #6a6a6a;
    --paper: #ffffff;
    --ink: #201d1b;
    --edge: #5a5a5a;
    --spine: #4a4a4a;
    --reverse: #f2f2f2;
  }
  * { box-sizing: border-box; margin: 0; padding: 0; }
  html, body {
    width: 1200px; height: 1000px; overflow: hidden;
    background: var(--backdrop);
  }
  .canvas { position: relative; width: 1200px; height: 1000px; }
  .cover-art { position: absolute; inset: 0; }
  .title {
    position: absolute; right: 236px; top: 280px;
    font-family: "Cormorant Garamond", serif;
    font-weight: 600; font-variant: small-caps;
    font-size: 46px; line-height: 1; letter-spacing: 1px;
    color: var(--ink);
  }
  .subtitle {
    position: absolute; right: 237px; top: 358px;
    font-family: "Open Sans", sans-serif;
    font-size: 13px; word-spacing: 4px;
    color: var(--ink);
  }
  .subtitle strong { font-weight: 700; }
  .author {
    position: absolute; right: 234px; top: 717px;
    font-family: "Open Sans", sans-serif;
    font-size: 15px; letter-spacing: 2.4px;
    color: var(--reverse);
  }
  .themes {
    position: absolute; left: 211px; top: 602px;
    list-style: none;
    font-family: "Open Sans", sans-serif;
    font-size: 12.5px; color: var(--ink);
  }
  .themes li { height: 68.5px; display: flex; align-items: flex-start; }
  .themes li::before {
    content: ""; width: 6px; height: 6px; margin: 5px 6px 0 0;
    background: var(--ink);
    clip-path: polygon(0 0, 0 100%, 100% 100%);
  }
</style>
</head>
<body>
<main class="canvas">
  <svg class="cover-art" width="1200" height="1000" viewBox="0 0 1200 1000" aria-hidden="true">
    <rect class="paper" x="200" y="215" width="800" height="570" fill="var(--paper)"/>
    <polygon class="back-panel" points="200,215 600,215 680,665 580,785 287,785 200,290"
             fill="var(--ink)" stroke="var(--edge)" stroke-width="2"/>
    <line class="spine" x1="600" y1="215" x2="600" y2="755" stroke="var(--spine)" stroke-width="1"/>
    <polygon class="author-band" points="686,670 1000,670 1000,785 628,785"
             fill="var(--ink)" stroke="var(--edge)" stroke-width="2"/>
  </svg>

  <h1 class="title">Tide &amp; Stone</h1>
  <p class="subtitle">Walk the <strong>Road</strong> of <strong>Still Waters</strong></p>
  <p class="author">OWEN HALVARY</p>

  <ul class="themes">
    <li>EGO</li>
    <li>WAR</li>
    <li>MONEY</li>
  </ul>
</main>
</body>
</html>
```